Criação de Kit com 6 Layouts de Post para Redes Sociais (Facebook, Instagram e etc) para Saúde & Nutrição
" Consultório oftalmológico com ênfase em consultas oftalmológicas, exames complementares e cirurgias oculares "

```html
<!DOCTYPE html>
<html lang="pt-BR">
<head>
<meta charset="utf-8">
<title>Cirurgia oftalmológica – post</title>
<link rel="stylesheet" href="https://fonts.googleapis.com/css2?family=Poppins:wght@400;500;600;700&display=swap">
<style>
  :root{
    --navy:#10294d;
    --sand:#e8d2ab;
    --white:#ffffff;
    --teal-dark:#173f4b;
    --teal-mid:#2c6a78;
    --cyan-light:#8fd6e6;
    --cyan-soft:#5bb8cc;
    --skin:#c7a394;
    --bokeh:#d8e4da;
  }
  html,body{margin:0;padding:0;overflow:hidden;}
  body{width:1200px;height:1200px;font-family:"Poppins",sans-serif;}
  .post{position:relative;width:1200px;height:1200px;overflow:hidden;background:var(--teal-dark);}
  .photo{
    position:absolute;inset:0;
    background:
      radial-gradient(ellipse 28% 22% at 14% 8%, rgba(216,228,218,.85) 0%, rgba(216,228,218,0) 70%),
      radial-gradient(ellipse 36% 30% at 72% 76%, rgba(143,214,230,1) 0%, rgba(111,196,214,.9) 45%, rgba(91,184,204,0) 80%),
      radial-gradient(ellipse 30% 18% at 80% 55%, rgba(168,220,232,.9) 0%, rgba(168,220,232,0) 75%),
      radial-gradient(ellipse 30% 16% at 78% 38%, rgba(199,163,148,.95) 0%, rgba(199,163,148,.6) 50%, rgba(199,163,148,0) 85%),
      radial-gradient(ellipse 36% 20% at 78% 12%, rgba(91,184,204,.95) 0%, rgba(91,184,204,0) 80%),
      radial-gradient(ellipse 50% 70% at 90% 60%, rgba(62,140,158,.9) 0%, rgba(62,140,158,0) 80%),
      linear-gradient(100deg, var(--teal-dark) 0%, #1e5260 40%, var(--teal-mid) 100%);
  }
  .badge{
    position:absolute;left:283px;top:283px;width:130px;height:130px;border-radius:50%;
    background:var(--white);z-index:2;
  }
  .panel{
    position:absolute;left:192px;top:343px;width:437px;height:520px;
    background:var(--navy);box-sizing:border-box;padding:118px 20px 0 38px;
  }
  .eyebrow{
    display:inline-block;background:var(--sand);color:var(--navy);
    font-weight:500;font-size:23px;line-height:1;padding:8px 16px;border-radius:6px;
  }
  .title{margin:4px 0 0;color:var(--white);line-height:1;}
  .title-main{display:block;font-weight:600;font-size:84px;line-height:1.05;}
  .title-sub{display:block;font-weight:500;font-size:48px;line-height:1.05;}
  .lead{margin:14px 0 0;color:var(--white);font-size:20px;line-height:1.28;font-weight:400;}
  .cta{
    position:absolute;left:38px;top:462px;display:flex;align-items:center;gap:12px;
    background:var(--sand);color:var(--navy);font-weight:500;font-size:21px;
    padding:8px 30px 8px 10px;border-radius:30px;
  }
  .cta svg{display:block}
  .brand{
    position:absolute;left:192px;top:990px;width:437px;text-align:center;color:var(--white);
  }
  .brand-title{display:block;font-size:14px;font-weight:400;letter-spacing:1px;line-height:1;}
  .brand-name{display:block;font-weight:500;font-size:27px;letter-spacing:1px;text-transform:uppercase;line-height:1.15;}
  .brand-role{display:block;font-size:13px;font-weight:400;letter-spacing:4px;line-height:1;}
</style>
</head>
<body>
<main class="post">
  <div class="photo" role="img" aria-label="Fotografia de uma cirurgiã oftalmológica de touca, máscara cirúrgica e óculos de proteção em centro cirúrgico em tons de azul-turquesa"></div>

  <div class="badge"></div>
  <section class="panel">
    <span class="eyebrow">Você já realizou</span>
    <h1 class="title">
      <span class="title-main">Cirurgia</span>
      <span class="title-sub">oftalmológica?</span>
    </h1>
    <p class="lead">Correções refrativas para problemas de visão até cirurgias para tratar condições como catarata, estrabismo, glaucoma e problemas das pálpebras.</p>
    <a class="cta">
      <svg width="30" height="30" viewBox="0 0 30 30" aria-hidden="true">
        <circle cx="15" cy="15" r="15" fill="#10294d"/>
        <path d="M12 9l6 6-6 6" fill="none" stroke="#ffffff" stroke-width="2.6" stroke-linecap="round" stroke-linejoin="round"/>
      </svg>
      Fale conosco
    </a>
  </section>

  <div class="brand">
    <span class="brand-title">DRA.</span>
    <span class="brand-name">Helena Duarte</span>
    <span class="brand-role">oftalmologista</span>
  </div>
</main>
</body>
</html>
```